Business Card for: Northbrook Financial Advisory Services Inc.

provide strategic financial advisory services to companies in the areas of corporate finance, mergers and acquisitions, executive coaching and strategic planning

Target Market(s)

Companies, banks, accountants, lawyers

Industry/Entity Type

High end business consulting in corporate finance, mergers and acquisitions, consulting

Contact Information for Business Card

Name of company, Name: xxxxxx xxxxxx , CEO, - phone number: 1-xxx-xxx-xxxx, - email address,

Requirements
Must have
• Must be professional and simple.
Nice to have
• simple, straight graphics, must give the impression that we are trustworthy, professional, competent
Should not have
• loud colors, loud design features

```html
<!DOCTYPE html>
<html lang="en">
<head>
<meta charset="utf-8">
<title>Northbrook Financial Advisory Inc — Business Card</title>
<link href="https://fonts.googleapis.com/css2?family=Montserrat:wght@300;400;500;700&display=swap" rel="stylesheet">
<style>
  :root {
    --backdrop: #8a8a8a;
    --card-dark: #151515;
    --card-light: #ffffff;
    --accent: #e8670f;
    --silver: #c4c4c4;
    --text-light: #ffffff;
    --text-dark: #1c1c1c;
    --text-web: #9a9a9a;
    --rule: #d6d6d6;
  }
  * { margin: 0; padding: 0; box-sizing: border-box; }
  html, body { width: 900px; height: 1200px; overflow: hidden; }
  body {
    background: var(--backdrop);
    font-family: "Montserrat", sans-serif;
    position: relative;
  }
  .card-slot { position: absolute; left: 153px; width: 594px; height: 338px; }
  .card-slot--front { top: 242px; }
  .card-slot--back { top: 620px; }
  .card {
    position: absolute; left: 0; top: 0;
    width: 396px; height: 225px;
    transform: scale(1.5); transform-origin: 0 0;
    overflow: hidden;
    box-shadow: 0 1px 3px rgba(0,0,0,.35);
  }
  .card--front { background: var(--card-dark); }
  .card--back { background: var(--card-light); }

  .accent-art { position: absolute; top: 0; width: 34px; height: 225px; }
  .accent-art--front {
    left: 0;
    background: linear-gradient(90deg, var(--accent) 0%, var(--silver) 55%, var(--card-dark) 100%);
  }
  .accent-art--back {
    right: 0;
    background: linear-gradient(270deg, var(--accent) 0%, var(--silver) 55%, var(--card-light) 100%);
  }

  .front-brand__name {
    position: absolute; top: 69px; left: 40px; right: 0; text-align: center;
    color: var(--accent); font-weight: 700; font-size: 20px; letter-spacing: .3px;
  }
  .front-brand__tagline {
    position: absolute; top: 93px; left: 40px; right: 0; text-align: center;
    color: var(--text-light); font-weight: 300; font-size: 19.5px;
  }
  .services { font-size: 6.3px; font-weight: 400; white-space: nowrap; }
  .services .dot {
    display: inline-block; width: 3.4px; height: 3.4px; border-radius: 50%;
    background: var(--accent); margin: 0 2px; vertical-align: 0.5px;
  }
  .front-services {
    position: absolute; top: 121px; left: 40px; right: 0; text-align: center;
    color: var(--text-light);
  }
  .front-services .dot:last-of-type { background: var(--text-light); }
  .front-web {
    position: absolute; top: 179px; left: 40px; right: 0; text-align: center;
    color: var(--text-web); font-size: 5.5px; letter-spacing: 1px;
  }

  .back-company {
    position: absolute; left: 30px; top: 50px;
    color: var(--text-dark); font-weight: 400; font-size: 14.2px;
  }
  .back-services { position: absolute; left: 30px; top: 71px; color: var(--text-dark); }
  .person { position: absolute; left: 34px; top: 128px; color: var(--text-dark); }
  .person__name { font-size: 10.4px; font-weight: 500; letter-spacing: .3px; }
  .person__role { font-size: 7.3px; font-weight: 400; margin-top: 1px; }
  .divider {
    position: absolute; left: 140px; top: 118px; width: 1px; height: 56px;
    background: linear-gradient(var(--card-light), var(--rule) 25%, var(--rule) 75%, var(--card-light));
  }
  .contacts { position: absolute; left: 154px; top: 122px; list-style: none; }
  .contacts li {
    display: flex; align-items: center; height: 16px;
    font-size: 7.4px; color: var(--text-dark);
  }
  .contacts svg { width: 6px; height: 6px; margin-right: 8px; fill: var(--accent); }
</style>
</head>
<body>

<div class="card-slot card-slot--front">
  <div class="card card--front">
    <div class="accent-art accent-art--front" role="img" aria-label="Decorative silver and orange curved band along the left edge"></div>
    <div class="front-brand__name">NORTHBROOK</div>
    <div class="front-brand__tagline">Financial Advisory Inc</div>
    <div class="services front-services">Corporate finance<span class="dot"></span>Mergers and Acquisitions<span class="dot"></span>Executive Coaching<span class="dot"></span>Strategic Planning</div>
    <div class="front-web">www.mywebsite.com</div>
  </div>
</div>

<div class="card-slot card-slot--back">
  <div class="card card--back">
    <div class="accent-art accent-art--back" role="img" aria-label="Decorative silver and orange curved band along the right edge"></div>
    <div class="back-company">Northbrook Financial Advisory Inc</div>
    <div class="services back-services">Corporate finance<span class="dot"></span>Mergers and Acquisitions<span class="dot"></span>Executive Coaching<span class="dot"></span>Strategic Planning</div>
    <div class="person">
      <div class="person__name">LOREM IPSUM</div>
      <div class="person__role">Director</div>
    </div>
    <div class="divider"></div>
    <ul class="contacts">
      <li><svg viewBox="0 0 10 10" aria-hidden="true"><path d="M2,0 L4,2.5 L3,3.8 C3.8,5.4 4.8,6.4 6.2,7 L7.5,6 L10,8 L8.5,10 C4,9.5 0.5,6 0,1.5 Z"/></svg>123 1234 123</li>
      <li><svg viewBox="0 0 10 10" aria-hidden="true"><path d="M0,2 H10 V8 H0 Z M0.6,2.4 L5,5.6 L9.4,2.4 V2.9 L5,6.2 L0.6,2.9 Z" fill-rule="evenodd"/></svg>my company@mail.com</li>
      <li><svg viewBox="0 0 10 10" aria-hidden="true"><circle cx="5" cy="5" r="4.6"/></svg>www.mywebsite.com</li>
    </ul>
  </div>
</div>

</body>
</html>
```